Bright Sprouts Business Card

speech therapy business card that is fun and professional using my logo.

Wow wonderful dedigns ... 

Industry/Entity Type

Business

Contact Information for Business Card

Rosa Vantrell
Corvid Certified Practising Speech Pathologist
B.Sp.Path MRTQB CRTP
ph: 0419364720
brightsprotsspeechpathology@mailtrove.example
www.brightsproutsspeechpathology.example

```html
<!DOCTYPE html>
<html lang="en">
<head>
<meta charset="utf-8">
<title>Bright Sprouts Speech Pathology – Business Card</title>
<link rel="stylesheet" href="https://fonts.googleapis.com/css2?family=Open+Sans:wght@400;600&display=swap">
<style>
  :root {
    --stage: #2b2b2b;
    --card-blue: #6abde8;
    --band-blue: #4a9dcd;
    --brand-blue: #3f86b8;
    --brand-purple: #6a2a6e;
    --white: #ffffff;
    --pale: #e9f5fc;
    --rule-text: #4a88b8;
  }
  * { margin: 0; padding: 0; box-sizing: border-box; }
  html, body { width: 1200px; height: 1000px; overflow: hidden; }
  body {
    position: relative;
    background: var(--stage);
    font-family: "Open Sans", Arial, sans-serif;
  }
  .card {
    position: absolute;
    left: 222px;
    width: 738px;
    height: 411px;
    background: var(--card-blue);
    overflow: hidden;
  }
  .card--front { top: 88px; }
  .card--back { top: 529px; }
  .glow {
    position: absolute;
    inset: 0;
    width: 100%;
    height: 100%;
  }
  .brand {
    position: absolute;
    display: flex;
    align-items: center;
    gap: 30px;
  }
  .brand__mark {
    width: 104px;
    height: 104px;
    border-radius: 50%;
    background: var(--brand-purple);
    flex: none;
  }
  .brand__name {
    color: var(--brand-blue);
    font-weight: 600;
    font-size: 30px;
    line-height: 1.15;
  }
  .card--front .brand { left: 116px; top: 169px; }
  .card--back .brand { left: 74px; top: 22px; }
  .card--back .brand__mark { display: none; }
  .web-band {
    position: absolute;
    right: 0;
    bottom: 0;
    width: 376px;
    height: 33px;
    background: var(--band-blue);
    clip-path: polygon(22px 0, 100% 0, 100% 100%, 0 100%);
    display: flex;
    align-items: center;
    justify-content: flex-end;
    padding-right: 12px;
    color: var(--white);
    font-size: 15px;
    white-space: nowrap;
  }
  .person {
    position: absolute;
    left: 438px;
    top: 181px;
    width: 297px;
  }
  .person__name {
    color: var(--white);
    font-size: 30px;
    line-height: 1;
    letter-spacing: -0.5px;
  }
  .person__role {
    margin-top: 4px;
    background: var(--pale);
    color: var(--rule-text);
    font-size: 8px;
    letter-spacing: 1.9px;
    text-transform: uppercase;
    text-align: right;
    padding: 4px 6px 4px 0;
    white-space: nowrap;
  }
  .person__quals {
    margin-top: 5px;
    color: var(--white);
    font-size: 12px;
    text-align: right;
    padding-right: 8px;
  }
  .contact-band {
    position: absolute;
    right: 0;
    top: 289px;
    width: 311px;
    height: 68px;
    background: var(--band-blue);
    clip-path: polygon(18px 0, 100% 0, 100% 100%, 0 100%);
    padding: 13px 0 0 24px;
    color: var(--white);
    font-size: 11.5px;
    line-height: 26px;
    white-space: nowrap;
  }
  .contact-band strong { font-weight: 600; }
  .side-label {
    position: absolute;
    left: 1043px;
    color: var(--white);
    font-size: 33px;
    letter-spacing: -0.5px;
  }
  .side-label--front { top: 268px; }
  .side-label--back { top: 709px; }
</style>
</head>
<body>

<section class="card card--front" aria-label="Card front">
  <svg class="glow" viewBox="0 0 738 411" aria-hidden="true">
    <defs>
      <radialGradient id="glow-front" cx="0.22" cy="0.55" r="0.45">
        <stop offset="0" stop-color="#ffffff" stop-opacity="0.55"/>
        <stop offset="1" stop-color="#ffffff" stop-opacity="0"/>
      </radialGradient>
    </defs>
    <rect width="738" height="411" fill="url(#glow-front)"/>
    <g fill="#ffffff" fill-opacity="0.08" stroke="#ffffff" stroke-opacity="0.35">
      <circle cx="-40" cy="80" r="82"/>
      <circle cx="130" cy="250" r="120"/>
      <circle cx="90" cy="370" r="70"/>
    </g>
  </svg>
  <div class="brand">
    <span class="brand__mark"></span>
    <span class="brand__name">Bright Sprouts<br>Speech Pathology</span>
  </div>
  <div class="web-band">www.brightsproutsspeechpathology.example</div>
</section>

<section class="card card--back" aria-label="Card back">
  <svg class="glow" viewBox="0 0 738 411" aria-hidden="true">
    <defs>
      <radialGradient id="glow-back" cx="0.22" cy="0.55" r="0.45">
        <stop offset="0" stop-color="#ffffff" stop-opacity="0.55"/>
        <stop offset="1" stop-color="#ffffff" stop-opacity="0"/>
      </radialGradient>
    </defs>
    <rect width="738" height="411" fill="url(#glow-back)"/>
    <g fill="#ffffff" fill-opacity="0.08" stroke="#ffffff" stroke-opacity="0.35">
      <circle cx="-40" cy="80" r="82"/>
      <circle cx="130" cy="250" r="120"/>
      <circle cx="90" cy="370" r="70"/>
    </g>
  </svg>
  <div class="brand">
    <span class="brand__mark"></span>
    <span class="brand__name">Bright Sprouts<br>Speech Pathology</span>
  </div>
  <div class="person">
    <p class="person__name">Rosa Vantrell</p>
    <p class="person__role">Corvid Certified Practising Speech Pathologist</p>
    <p class="person__quals">B.Sp.Path MRTQB CRTP</p>
  </div>
  <div class="contact-band">
    <p><strong>ph:</strong> 0419364720</p>
    <p>brightsprotsspeechpathology@mailtrove.example</p>
  </div>
</section>

<p class="side-label side-label--front">Front</p>
<p class="side-label side-label--back">Back</p>

</body>
</html>
```